Design for online reviews widget

Attached is a wireframe of a widget we need designing to display reviews on websites from multiple sources. We need this provided at 3 different sizes including full screen, contained (like the wireframe) and mobile.
You have completely free rein on the styling.
The only elements that should remain untouched are the blue stars (https://www.filquarry.net/s/8vtmwp2291zq4h/kv%20stars.ai?dl=0) and powered by logo at the bottom.
Ignore the menu at the top of the wireframe, this is just from the website the widget will be placed on.
Businesses

```html
<!DOCTYPE html>
<html lang="en">
<head>
<meta charset="utf-8">
<title>Reviews widget</title>
<link href="https://fonts.googleapis.com/css2?family=Figtree:wght@400;500;600;700&display=swap" rel="stylesheet">
<style>
:root{
  --blue:#1ba8e0;
  --ink:#111;
  --body:#666;
  --line:#d6d6d6;
  --panel:#f4f4f4;
  --green:#5cb917;
  --gold:#f7c21b;
  --score-blue:#0d4f9c;
}
*{box-sizing:border-box;margin:0;padding:0}
html,body{width:1062px;height:1200px;overflow:hidden;background:#fff;font-family:"Figtree",sans-serif;color:var(--ink)}
.widget{position:relative;width:1062px;height:1200px}
.summary{height:100px;border-bottom:1px solid var(--line);position:relative}
.summary-stars{position:absolute;left:88px;top:30px;display:flex;gap:6px}
.summary-stars svg{width:36px;height:36px}
.summary-text{position:absolute;left:313px;top:27px}
.summary-label{font-size:16px;font-weight:400}
.summary-score{font-size:20px;font-weight:700;color:var(--blue);margin-top:1px}
.filter{position:absolute;left:793px;top:27px;width:192px;height:38px;border:1px solid #bbb;display:flex;align-items:center;justify-content:space-between;padding:0 14px 0 16px;font-size:13px;color:#444}
.reviews{background:var(--panel);height:960px;padding-top:57px;border-bottom:1px solid var(--line)}
.review{margin:0 0 16px 69px;width:931px;background:#fff;border:1px solid var(--line);display:flex;padding:26px 0 0 40px}
.review-main{flex:1}
.review-title{font-size:17.5px;font-weight:700;line-height:22px;margin-bottom:9px}
.review-body{font-size:11.4px;line-height:19.6px;color:var(--body);max-width:690px;letter-spacing:.1px}
.ratings{display:flex;gap:24px;font-size:12.5px;margin-top:10px}
.ratings b{font-weight:700}
.service{font-size:12.5px;margin-top:12px}
.meta{display:flex;gap:22px;font-size:12.5px;margin-top:12px;align-items:center}
.meta span{display:flex;align-items:center;gap:8px}
.source{width:200px;display:flex;flex-direction:column;align-items:center;padding-top:12px}
.source-name{font-size:24px;font-weight:700;color:#333;display:flex;align-items:center;gap:8px}
.source-dot{width:18px;height:18px;border-radius:50%;background:var(--score-blue)}
.source-score{font-size:40px;font-weight:700;color:var(--score-blue);margin-top:22px;line-height:1}
.rating-stars{display:flex;gap:4px;margin-top:10px}
.rating-stars svg{width:22px;height:22px}
.load-more{position:absolute;left:436px;top:1039px;width:194px;height:53px;border-radius:27px;background:var(--green);color:#fff;font-size:17px;font-weight:700;display:flex;align-items:center;justify-content:center;gap:6px}
.powered{position:absolute;left:784px;top:1094px;width:182px;text-align:right}
.powered-label{font-size:14px;font-weight:500;margin-right:42px}
.powered-name{font-size:22px;font-weight:700;display:flex;align-items:center;justify-content:flex-end;gap:8px;margin-top:6px}
.powered-dot{width:20px;height:20px;border-radius:50%;background:var(--blue)}
</style>
</head>
<body>
<div class="widget">
  <header class="summary">
    <div class="summary-stars">
      <svg viewBox="0 0 36 36"><circle cx="18" cy="18" r="18" fill="#1ba8e0"/><path d="M18 7l3.3 6.9 7.5.9-5.5 5.2 1.4 7.5L18 23.8l-6.7 3.7 1.4-7.5-5.5-5.2 7.5-.9z" fill="#fff"/></svg>
      <svg viewBox="0 0 36 36"><circle cx="18" cy="18" r="18" fill="#1ba8e0"/><path d="M18 7l3.3 6.9 7.5.9-5.5 5.2 1.4 7.5L18 23.8l-6.7 3.7 1.4-7.5-5.5-5.2 7.5-.9z" fill="#fff"/></svg>
      <svg viewBox="0 0 36 36"><circle cx="18" cy="18" r="18" fill="#1ba8e0"/><path d="M18 7l3.3 6.9 7.5.9-5.5 5.2 1.4 7.5L18 23.8l-6.7 3.7 1.4-7.5-5.5-5.2 7.5-.9z" fill="#fff"/></svg>
      <svg viewBox="0 0 36 36"><circle cx="18" cy="18" r="18" fill="#1ba8e0"/><path d="M18 7l3.3 6.9 7.5.9-5.5 5.2 1.4 7.5L18 23.8l-6.7 3.7 1.4-7.5-5.5-5.2 7.5-.9z" fill="#fff"/></svg>
      <svg viewBox="0 0 36 36"><circle cx="18" cy="18" r="18" fill="#1ba8e0"/><path d="M18 7l3.3 6.9 7.5.9-5.5 5.2 1.4 7.5L18 23.8l-6.7 3.7 1.4-7.5-5.5-5.2 7.5-.9z" fill="#fff"/></svg>
    </div>
    <div class="summary-text">
      <div class="summary-label">Combined Review Score</div>
      <div class="summary-score">4.3 out of 5</div>
    </div>
    <div class="filter">Filter by
      <svg width="12" height="8" viewBox="0 0 12 8"><path d="M1 1l5 5 5-5" stroke="#666" stroke-width="1.6" fill="none"/></svg>
    </div>
  </header>

  <section class="reviews">
    <article class="review" style="height:207px">
      <div class="review-main">
        <h2 class="review-title">Front door with windows each side and side window</h2>
        <p class="review-body">This is the second time we have used Regent Home Improvments , and the service is amazing! Martin came round several times as we keep changing our minds and he was so helpful and gave us good advice, and the guys who do the fitting are efficient and tidy . I've got to say the end result is amazing and I have recommended to many of friends . Thanks Regent</p>
        <div class="ratings"><span>Reliablity: <b>9.38</b></span><span>Courtesy: <b>10</b></span><span>Tidiness: <b>9.84</b></span><span>Workmanship: <b>10</b></span></div>
        <div class="meta">
          <span><svg width="17" height="17" viewBox="0 0 17 17"><circle cx="8.5" cy="8.5" r="7.3" fill="none" stroke="#5cb917" stroke-width="2"/><path d="M8.5 4.5v4.3H5.5" stroke="#5cb917" stroke-width="1.6" fill="none"/></svg>Verified 28th September 2021</span>
          <span><svg width="14" height="19" viewBox="0 0 14 19"><path d="M7 0a7 7 0 017 7c0 5-7 12-7 12S0 12 0 7a7 7 0 017-7z" fill="#5cb917"/><circle cx="7" cy="7" r="2.5" fill="#fff"/></svg>Located in Oakfield</span>
        </div>
      </div>
      <div class="source" style="padding-top:24px">
        <div class="source-name" style="color:#e52d2d">TradeScore</div>
        <div class="source-score">9.77</div>
      </div>
    </article>

    <article class="review" style="height:208px">
      <div class="review-main">
        <h2 class="review-title">Positive: Professionalism, Quality, Value</h2>
        <p class="review-body">The team did a good job of replacing a large feature window spanning two floors, as well as the others in my property. They're a professional group who were willing to work out solutions to any problem, especially compared to other companies. Prices are fair, and my new UPVC windows look great. Special thanks to Colin for being so accommodating and for the good communication throughout.</p>
        <div class="service">Service: <b>Window installation</b></div>
        <div class="meta"><span><svg width="17" height="17" viewBox="0 0 17 17"><circle cx="8.5" cy="8.5" r="7.3" fill="none" stroke="#5cb917" stroke-width="2"/><path d="M8.5 4.5v4.3H5.5" stroke="#5cb917" stroke-width="1.6" fill="none"/></svg>11 months ago by Daniel Hart</span></div>
      </div>
      <div class="source" style="padding-top:30px">
        <div class="source-name" style="color:#4a7fd8">Searchly</div>
        <div class="rating-stars">
          <svg viewBox="0 0 24 24"><path d="M12 1l3.4 7 7.6.9-5.6 5.3 1.5 7.6L12 18l-6.9 3.8 1.5-7.6L1 8.9 8.6 8z" fill="#f7c21b"/></svg>
          <svg viewBox="0 0 24 24"><path d="M12 1l3.4 7 7.6.9-5.6 5.3 1.5 7.6L12 18l-6.9 3.8 1.5-7.6L1 8.9 8.6 8z" fill="#f7c21b"/></svg>
          <svg viewBox="0 0 24 24"><path d="M12 1l3.4 7 7.6.9-5.6 5.3 1.5 7.6L12 18l-6.9 3.8 1.5-7.6L1 8.9 8.6 8z" fill="#f7c21b"/></svg>
          <svg viewBox="0 0 24 24"><path d="M12 1l3.4 7 7.6.9-5.6 5.3 1.5 7.6L12 18l-6.9 3.8 1.5-7.6L1 8.9 8.6 8z" fill="#f7c21b"/></svg>
          <svg viewBox="0 0 24 24"><path d="M12 1l3.4 7 7.6.9-5.6 5.3 1.5 7.6L12 18l-6.9 3.8 1.5-7.6L1 8.9 8.6 8z" fill="#f7c21b"/></svg>
        </div>
      </div>
    </article>

    <article class="review" style="height:196px">
      <div class="review-main">
        <h2 class="review-title">Brilliant all round professional, friendly service.</h2>
        <p class="review-body">This home run friendly business was a real pleasure to deal with. From the professional, no pressure quote, nothing was too much trouble to ensure everything is as required for your needs with the quote and fitting. The workmanship and double glazing being fitted was brilliant and my home/outdoors was left tidy and clean leaving an outstanding impression for such an all round professional job. I would not hesitate to recommend this company, such a brilliant service from great hardworking people that care about their service.</p>
        <div class="meta"><span><svg width="17" height="17" viewBox="0 0 17 17"><circle cx="8.5" cy="8.5" r="7.3" fill="none" stroke="#5cb917" stroke-width="2"/><path d="M8.5 4.5v4.3H5.5" stroke="#5cb917" stroke-width="1.6" fill="none"/></svg>13 Feb 2018 by GreenChair42</span></div>
      </div>
      <div class="source" style="padding-top:26px">
        <div class="source-name"><span class="source-dot" style="background:#f7d117"></span>Listora</div>
        <div class="rating-stars">
          <svg viewBox="0 0 24 24"><path d="M12 1l3.4 7 7.6.9-5.6 5.3 1.5 7.6L12 18l-6.9 3.8 1.5-7.6L1 8.9 8.6 8z" fill="#f7d117"/></svg>
          <svg viewBox="0 0 24 24"><path d="M12 1l3.4 7 7.6.9-5.6 5.3 1.5 7.6L12 18l-6.9 3.8 1.5-7.6L1 8.9 8.6 8z" fill="#f7d117"/></svg>
          <svg viewBox="0 0 24 24"><path d="M12 1l3.4 7 7.6.9-5.6 5.3 1.5 7.6L12 18l-6.9 3.8 1.5-7.6L1 8.9 8.6 8z" fill="#f7d117"/></svg>
          <svg viewBox="0 0 24 24"><path d="M12 1l3.4 7 7.6.9-5.6 5.3 1.5 7.6L12 18l-6.9 3.8 1.5-7.6L1 8.9 8.6 8z" fill="#f7d117"/></svg>
          <svg viewBox="0 0 24 24"><path d="M12 1l3.4 7 7.6.9-5.6 5.3 1.5 7.6L12 18l-6.9 3.8 1.5-7.6L1 8.9 8.6 8z" fill="#f7d117"/></svg>
        </div>
      </div>
    </article>

    <article class="review" style="height:188px">
      <div class="review-main">
        <h2 class="review-title">Front door with windows each side and side window</h2>
        <p class="review-body">This is the second time we have used Regent Home Improvments , and the service is amazing! Martin came round several times as we keep changing our minds and he was so helpful and gave us good advice, and the guys who do the fitting are efficient and tidy . I've got to say the end result is amazing and I have recommended to many of friends . Thanks Regent</p>
        <div class="meta"><span><svg width="17" height="17" viewBox="0 0 17 17"><circle cx="8.5" cy="8.5" r="7.3" fill="none" stroke="#5cb917" stroke-width="2"/><path d="M8.5 4.5v4.3H5.5" stroke="#5cb917" stroke-width="1.6" fill="none"/></svg>13 Feb 2018 by Kate</span></div>
      </div>
      <div class="source" style="padding-top:14px">
        <div class="source-name">TrustNest</div>
        <div class="rating-stars">
          <svg viewBox="0 0 24 24"><path d="M12 1l3.4 7 7.6.9-5.6 5.3 1.5 7.6L12 18l-6.9 3.8 1.5-7.6L1 8.9 8.6 8z" fill="#f7c21b"/></svg>
          <svg viewBox="0 0 24 24"><path d="M12 1l3.4 7 7.6.9-5.6 5.3 1.5 7.6L12 18l-6.9 3.8 1.5-7.6L1 8.9 8.6 8z" fill="#f7c21b"/></svg>
          <svg viewBox="0 0 24 24"><path d="M12 1l3.4 7 7.6.9-5.6 5.3 1.5 7.6L12 18l-6.9 3.8 1.5-7.6L1 8.9 8.6 8z" fill="#f7c21b"/></svg>
          <svg viewBox="0 0 24 24"><path d="M12 1l3.4 7 7.6.9-5.6 5.3 1.5 7.6L12 18l-6.9 3.8 1.5-7.6L1 8.9 8.6 8z" fill="#f7c21b"/></svg>
          <svg viewBox="0 0 24 24"><path d="M12 1l3.4 7 7.6.9-5.6 5.3 1.5 7.6L12 18l-6.9 3.8 1.5-7.6L1 8.9 8.6 8z" fill="#f7c21b"/></svg>
        </div>
      </div>
    </article>
  </section>

  <div class="load-more">LOAD MORE
    <svg width="16" height="10" viewBox="0 0 16 10"><path d="M2 2l6 6 6-6" stroke="#fff" stroke-width="2.4" fill="none"/></svg>
  </div>

  <footer class="powered">
    <div class="powered-label">Powered by</div>
    <div class="powered-name"><span class="powered-dot"></span>ReviewLoom</div>
  </footer>
</div>
</body>
</html>
```